Company Website for Zorvel Analytics, an open source data analytics company focused on relationship and li

I need a company/brand website for our new startup, Zorvel Analytics LLC. We are a company focused on using life pattern analysis techniques, looking at relationships and how relationships, attributes, and activity cluster to infer aggregate information about individuals and groups. Our focus is on improving the digital advertising market.

We have a company logo which I will upload shortly.

Target Market(s)

Digital Advertising

Number of Pages Required

3 page

Font styles to use
Sans Serif

Requirements
Must have
• An main page, about us, contact page.
Nice to have
• Zorvel Analytics relies on state of the art analytics applied to a the digital marketing space. While it is heavy in science, we also understand the art of influence. The website should have a scientific edge but also a flair that illustrates our focus on applying the hard science and analytics to influencing the behavior of people.

```html
<!DOCTYPE html>
<html lang="en">
<head>
<meta charset="utf-8">
<title>Zorvel Analytics</title>
<link rel="stylesheet" href="https://fonts.googleapis.com/css2?family=Montserrat:wght@400;500;600;700&family=Roboto:ital,wght@1,400&display=swap">
<style>
:root{
  --orange:#f7931e;
  --ink:#1f1f1f;
  --navy:#10304f;
  --grey-text:#8a8a8a;
  --panel:#f3f3f3;
  --hero:#2f3134;
  --footer:#151515;
  --white:#ffffff;
}
*{margin:0;padding:0;box-sizing:border-box}
html,body{width:710px;height:1200px;overflow:hidden;background:var(--white)}
body{position:relative;font-family:'Montserrat',sans-serif;color:var(--ink)}
.abs{position:absolute}
.hero-photo{left:0;top:0;width:710px;height:310px;background:linear-gradient(180deg,#3a3c3f 0%,#2a2c2f 55%,#3b3d40 100%)}
.brand{left:60px;top:16px;color:var(--white);font-weight:700;font-size:13px;display:flex;align-items:center;gap:5px;line-height:1}
.brand .dot{width:8px;height:8px;border-radius:50%;background:var(--white)}
.nav a{position:absolute;top:17px;font-size:7.5px;font-weight:600;color:var(--white);text-decoration:none}
.nav .active::before{content:"";position:absolute;left:-2px;right:-2px;top:-17px;height:2px;background:var(--orange)}
.nav .phone{font-weight:400;color:#d8d8d8;display:flex;align-items:center;gap:4px}
.hero-title{left:0;width:710px;top:95px;text-align:center;color:var(--white);font-weight:600;font-size:20.5px;line-height:23px}
.hero-sub{left:0;width:710px;top:150px;text-align:center;color:#e8e8e8;font-size:11px}
.btn{display:flex;align-items:center;justify-content:center;background:var(--orange);color:var(--white);font-weight:600;font-size:8px;text-decoration:none;box-shadow:0 2px 3px rgba(0,0,0,.15)}
.hero-btn{left:310px;top:181px;width:85px;height:22px}
.divider{left:0;top:258px}
.about-panel{left:351px;top:300px;width:359px;height:340px;background:var(--panel)}
.about-title{left:72px;top:333px;width:240px;font-weight:500;font-size:16px;line-height:20px}
.about-body{left:72px;top:408px;width:210px;font-size:6.4px;line-height:15.2px;color:var(--grey-text)}
.about-btn{left:74px;top:551px;width:81px;height:23px}
.quote{left:422px;top:359px;width:215px;font-family:'Roboto',sans-serif;font-style:italic;font-size:11.3px;line-height:21.5px;color:var(--navy)}
.cite{left:422px;top:524px;color:var(--navy)}
.cite strong{display:block;font-size:9.5px;font-weight:600;padding-left:16px;position:relative}
.cite strong::before{content:"";position:absolute;left:0;top:5px;width:9px;height:1.5px;background:var(--navy)}
.cite span{display:block;font-size:7.5px;padding-left:17px;color:var(--ink)}
.quote-mark{left:572px;top:488px;font-family:'Montserrat',sans-serif;font-weight:700;font-size:120px;line-height:1;color:#e2e2e2}
.dots{display:flex;gap:6px}
.dots i{width:4px;height:4px;border-radius:50%;background:#cfcfcf}
.dots i.on{background:var(--navy)}
.quote-dots{left:425px;top:568px}
.services{left:0;top:622px;width:710px;height:180px}
.service{position:absolute;top:0;height:180px;display:flex;flex-direction:column;align-items:center;justify-content:flex-end;padding-bottom:58px;color:var(--white);font-weight:500;font-size:10.5px;line-height:13px;text-align:center}
.service svg{margin-bottom:14px}
.service.one{left:0;width:235px;background:linear-gradient(135deg,#3d3e40,#252628)}
.service.two{left:235px;width:236px;background:linear-gradient(135deg,#f5a23a,#ef9224)}
.service.three{left:471px;width:239px;background:linear-gradient(135deg,#2b2c2e,#444547)}
.services-cut{left:0;top:620px}
.partners-title{left:0;width:710px;top:829px;text-align:center;font-weight:500;font-size:13.5px}
.partner{top:867px;width:117px;height:50px;border:1px solid #e2e2e2;display:flex;align-items:center;justify-content:center;gap:6px;font-weight:600;font-size:12px;color:#3a3a3a}
.partner b{width:10px;height:10px;border-radius:50%;background:#6a6a6a}
.partner-dots{left:326px;top:938px;gap:8px}
.partner-dots i{width:4px;height:4px;background:var(--orange)}
.partner-dots i.on{width:7px;height:7px;margin-top:-1.5px;background:none;border:1.5px solid var(--orange);position:relative}
.footer{left:0;top:972px;width:710px;height:228px;background:linear-gradient(180deg,#1b1b1b,#111)}
.sub-label{left:113px;top:998px;color:var(--white);font-size:8.5px;line-height:12px}
.sub-label strong{display:block;font-weight:600;font-size:9.5px}
.field{top:1002px;height:19px;border:1px solid #6e6e6e;color:var(--white);font-size:5.5px;padding:6px 7px}
.subscribe{left:504px;top:1001px;width:74px;height:21px;border:1px solid var(--orange);color:var(--orange);font-size:7px;font-weight:700;display:flex;align-items:center;justify-content:center}
.rule{left:113px;width:468px;height:1px;background:#3a3a3a}
.foot-brand{left:111px;top:1056px;color:var(--white);font-weight:700;font-size:10px;display:flex;align-items:center;gap:4px}
.foot-brand .dot{width:6px;height:6px;border-radius:50%;background:var(--white)}
.contact{left:113px;top:1082px;color:#e6e6e6;font-size:6.8px;line-height:13.5px}
.contact div{display:flex;align-items:center;gap:5px}
.col{top:1056px;color:#e6e6e6}
.col h4{font-size:7.8px;font-weight:600;margin-bottom:6px;color:var(--white)}
.col li{list-style:none;font-size:6.5px;line-height:12px}
.copyright{left:113px;top:1161px;color:#d8d8d8;font-size:5.6px}
.social{left:555px;top:1160px;display:flex;gap:3px}
.social i{width:11px;height:11px;border:1px solid #d8d8d8;border-radius:50%}
</style>
</head>
<body>

<div class="abs hero-photo" role="img" aria-label="Dark aerial photograph of a dense city skyline"></div>

<div class="abs brand"><span class="dot"></span>Zorvel Analytics</div>

<nav class="nav">
  <a class="active" style="left:410px" href="#">About us</a>
  <a style="left:464px" href="#">Contact page</a>
  <a style="left:530px" href="#">Random page</a>
  <a class="phone" style="left:600px" href="#">
    <svg width="7" height="7" viewBox="0 0 10 10"><path d="M2 0.5 L3.8 0.5 L4.4 3 L3.2 3.8 Q4.2 6 6.2 6.8 L7 5.6 L9.5 6.2 L9.5 8 Q9.5 9.5 8 9.5 Q0.5 9 0.5 2 Q0.5 0.5 2 0.5Z" fill="#d8d8d8"/></svg>
    +1 555 014 2290
  </a>
</nav>

<h1 class="abs hero-title">We relie on state of the art analytics<br>applied to a the digital marketing space</h1>
<p class="abs hero-sub">While it is heavy in science, we also understand the art of influence</p>
<a class="abs btn hero-btn" href="#">Get Started</a>

<svg class="abs divider" width="710" height="50" viewBox="0 0 710 50">
  <polygon points="0,6 496,46 710,6 710,50 0,50" fill="#ffffff"/>
  <polygon points="351,34 496,46 710,6 710,50 351,50" fill="#f3f3f3"/>
  <polyline points="0,6 496,46 710,6" fill="none" stroke="#f7931e" stroke-width="5"/>
</svg>

<div class="abs about-panel"></div>

<svg class="abs" style="left:336px;top:278px" width="28" height="28" viewBox="0 0 28 28">
  <circle cx="14" cy="14" r="14" fill="#f7931e"/>
  <polyline points="9,11.5 14,16.5 19,11.5" fill="none" stroke="#fff" stroke-width="2" stroke-linecap="round" stroke-linejoin="round"/>
</svg>

<h2 class="abs about-title">We are a company focused on using life pattern analysis techniques</h2>
<p class="abs about-body">Lorem ipsum dolor sit amet, consectetuer adipiscing elit. Aenean commodo ligula eget dolor. Aenean massa. Cum sociis natoque penatibus et magnis dis parturient montes, nascetur ridiculus mus. Donec quam felis, ultricies nec, pellentesque eu, pretium quis, sem. Nulla consequat massa quis enim. Donecporttitor eu, consequat vitae, eleifend ac, enim. Aliquam lorem ante, dapibus in, viverra quis, feugiat a, tellus. Phasel</p>
<a class="abs btn about-btn" href="#">Get Started</a>

<div class="abs quote-mark" aria-hidden="true">&rdquo;</div>
<blockquote class="abs quote">Lorem ipsum dolor sit amet, consectetuer adipiscing elit. Aenean commodo ligula eget dolor. Aenean massa. Cum sociis natoque penatibus et magnis dis parturient montes, nascetur ridiculus mus. Donec quam felis, ultricies nec, pellentesque eu, pretium quis, sem.</blockquote>
<div class="abs cite"><strong>Dara Wendt</strong><span>Company, CEO</span></div>
<div class="abs dots quote-dots"><i></i><i class="on"></i><i></i><i></i><i></i></div>

<section class="abs services">
  <div class="service one" role="img" aria-label="Photograph of a desk with a laptop and coffee cup">
    <svg width="44" height="38" viewBox="0 0 44 38" fill="none" stroke="#fff" stroke-width="1.6" stroke-linecap="round">
      <circle cx="24" cy="18" r="9"/><circle cx="24" cy="16" r="3"/><path d="M19 23 Q24 18 29 23"/>
      <line x1="17" y1="25" x2="6" y2="35"/><path d="M12 17 Q14 11 20 9 M36 17 Q34 11 28 9"/>
      <line x1="24" y1="2" x2="24" y2="5"/><line x1="16" y1="4" x2="18" y2="6"/><line x1="32" y1="4" x2="30" y2="6"/>
    </svg>
    Target Audience<br>Research
  </div>
  <div class="service two" role="img" aria-label="Orange-tinted photograph of a team joining hands over a table">
    <svg width="36" height="38" viewBox="0 0 36 38" fill="none" stroke="#fff" stroke-width="1.6">
      <rect x="2" y="2" width="26" height="24" rx="1"/><line x1="2" y1="7" x2="28" y2="7"/>
      <rect x="6" y="11" width="10" height="9"/><rect x="18" y="17" width="15" height="19" rx="1"/>
      <line x1="21" y1="22" x2="30" y2="22"/><circle cx="22" cy="27" r=".8"/><circle cx="25.5" cy="27" r=".8"/><circle cx="29" cy="27" r=".8"/><circle cx="22" cy="31" r=".8"/><circle cx="25.5" cy="31" r=".8"/><circle cx="29" cy="31" r=".8"/>
    </svg>
    Audience Impact<br>Calculation
  </div>
  <div class="service three" role="img" aria-label="Photograph of people reviewing financial papers beside a laptop">
    <svg width="42" height="40" viewBox="0 0 42 40" fill="none" stroke="#fff" stroke-width="1.6" stroke-linecap="round">
      <path d="M4 6 L20 6 M4 6 L4 36 L26 36"/><line x1="8" y1="12" x2="16" y2="12"/><line x1="8" y1="17" x2="14" y2="17"/>
      <rect x="14" y="18" width="24" height="14" rx="1"/><circle cx="26" cy="25" r="4"/>
      <path d="M22 10 L28 4 L32 8 L38 2 M34 2 L38 2 L38 6"/>
    </svg>
    Completele Revenue<br>Calculation
  </div>
</section>
<svg class="abs services-cut" width="710" height="20" viewBox="0 0 710 20"><polygon points="0,0 710,0 0,20" fill="#ffffff"/></svg>

<h3 class="abs partners-title">Our Partners</h3>
<div class="abs partner" style="left:98px"><b></b>Kestrel</div>
<div class="abs partner" style="left:226px">Ordana</div>
<div class="abs partner" style="left:352px">Veltrix</div>
<div class="abs partner" style="left:480px">Lumaro</div>
<div class="abs dots partner-dots"><i class="on"></i><i></i><i></i><i></i></div>

<footer class="abs footer" role="img" aria-label="Very dark city skyline photograph behind the footer"></footer>
<div class="abs sub-label">Subscribe<strong>For Our Newsletter</strong></div>
<div class="abs field" style="left:240px;width:94px">Full Name..</div>
<div class="abs field" style="left:340px;width:137px">Email Address..</div>
<div class="abs subscribe">Subscribe</div>
<div class="abs rule" style="top:1035px"></div>

<div class="abs foot-brand"><span class="dot"></span>Zorvel Analytics</div>
<div class="abs contact">
  <div><svg width="7" height="7" viewBox="0 0 10 10"><path d="M2 0.5 L3.8 0.5 L4.4 3 L3.2 3.8 Q4.2 6 6.2 6.8 L7 5.6 L9.5 6.2 L9.5 8 Q9.5 9.5 8 9.5 Q0.5 9 0.5 2 Q0.5 0.5 2 0.5Z" fill="#e6e6e6"/></svg>+1 555 014 2290</div>
  <div><svg width="7" height="6" viewBox="0 0 10 8"><rect x=".5" y=".5" width="9" height="7" fill="none" stroke="#e6e6e6"/><polyline points=".5,.5 5,4.5 9.5,.5" fill="none" stroke="#e6e6e6"/></svg>info@zorvelanalytics.com</div>
  <div style="padding-left:12px">Company Name</div>
</div>

<div class="abs col" style="left:259px"><h4>About Norvik Labs</h4><ul><li>Newsletter</li><li>Our Memberships</li><li>Events</li><li>Investors</li><li>Suppliers Response</li></ul></div>
<div class="abs col" style="left:393px"><h4>Account</h4><ul><li>Manage Your ID</li><li>Zorvel Store</li><li>Customer Reveiws</li><li>Ask a Question</li><li>Why choose us?</li></ul></div>
<div class="abs col" style="left:514px"><h4>Apie Mus</h4><ul><li>Inclusion and Diversity</li><li>Supplier Responsibility</li><li>Inclusion and Diversity</li><li>Shop for Business</li><li>Shop for Consumers</li></ul></div>

<div class="abs rule" style="top:1154px"></div>
<p class="abs copyright">Copyright 2018 Norvik Labs | All rights reserved</p>
<div class="abs social"><i></i><i></i><i></i></div>

</body>
</html>
```